"Sun On Water" Gospel Presentation Booklet

I need a design for a 12 page (including front/back cover) square booklet, with religious images and aesthetically pleasing fonts/designs. I want it to be very simple, and very straightforward. The main focus of the project is it's content. So the design should be very nice, but also should point to the content, not take away from it, or create distraction. People should be more focused on the words than the imagery.

I enjoy modern designs, I need a sharp aesthetic that is clean and neat. Nothing over the top.
I have attached a word document with the content I would like on the pages.

Colors
0592cd
0255a3
33a6d7
85cae6
85acd3
3276b5
9bcb3b
f04a50
f68d4c

Requirements
Should not have
• Super feminine colors/aesthetics

```html
<!DOCTYPE html>
<html lang="en">
<head>
<meta charset="utf-8">
<title>Sun On Water – Gospel Presentation Booklet</title>
<link rel="stylesheet" href="https://fonts.googleapis.com/css2?family=Raleway:wght@400;500;700;800&family=Pinyon+Script&display=swap">
<style>
  :root{
    --bg:#ececec;
    --page-dark:#333436;
    --teal:#2b8fb0;
    --sky:#33a6d7;
    --sky-light:#85cae6;
    --accent-blue:#3aa8de;
    --photo-gray-a:#9a9a9a;
    --photo-gray-b:#3d3d3d;
    --photo-teal-a:#3f8fa8;
    --photo-teal-b:#1f5366;
    --white:#ffffff;
    --dot:#6a6a6a;
  }
  *{box-sizing:border-box;margin:0;padding:0}
  html,body{width:1200px;height:1071px;overflow:hidden;background:var(--bg)}
  body{position:relative;font-family:"Raleway",sans-serif;color:var(--white);font-variant-numeric:lining-nums}

  .cover,.spread{position:absolute;overflow:hidden}
  .spread{display:flex}
  .page{position:relative;flex:1 1 50%;height:100%;overflow:hidden;background:var(--page-dark)}
  .photo{position:absolute;background:linear-gradient(160deg,var(--photo-gray-a),var(--photo-gray-b))}
  .photo--teal{background:linear-gradient(150deg,var(--photo-teal-a),var(--photo-teal-b))}
  .fill{inset:0}

  /* Cover */
  .cover{left:245px;top:35px;width:320px;height:320px}
  .cover__sky{position:absolute;inset:0;background:linear-gradient(180deg,#1f8fd6 0%,var(--sky) 45%,var(--sky-light) 80%,#e4f3fb 100%)}
  .cover__frame{position:absolute;left:60px;top:107px;width:194px;height:174px;border:2px solid var(--white)}
  .cover__quote{position:absolute;left:132px;top:82px;height:40px;padding:0 10px;font:800 64px/1 "Raleway",sans-serif;background:#269ad9}
  .cover__title{position:absolute;left:60px;top:140px;width:194px;text-align:center;font:800 54px/1 "Raleway",sans-serif;letter-spacing:1px}
  .cover__subtitle{position:absolute;left:60px;top:202px;width:194px;text-align:center;font:700 25px/1 "Raleway",sans-serif}

  .label{position:absolute;font:800 58px/1 "Raleway",sans-serif;letter-spacing:2px;display:flex;align-items:center;padding:0 12px;white-space:nowrap}
  .label--teal{background:var(--teal)}
  .label--dark{background:rgba(60,60,62,.92)}
  .rule{position:absolute;height:1px;background:var(--white)}
  .body{position:absolute;font-weight:500;letter-spacing:.8px}

  /* Spread 1 – God */
  .spread--god{left:608px;top:83px;width:576px;height:277px}
  .god__label{left:0;top:180px;width:203px;height:65px}
  .god__script{position:absolute;left:60px;top:60px;font:400 72px/1 "Pinyon Script",cursive}
  .god__kicker{position:absolute;left:128px;top:138px;font:800 17px/1 "Raleway",sans-serif;letter-spacing:2.5px}
  .god__body{left:90px;top:160px;width:190px;font-size:13.5px;line-height:22px}

  /* Spread 2 – Man */
  .spread--man{left:40px;top:420px;width:538px;height:273px}
  .man__label{left:53px;top:173px;width:214px;height:80px;font-size:64px;z-index:2}
  .man__heading{position:absolute;left:68px;top:160px;font:700 18px/1 "Raleway",sans-serif;letter-spacing:.6px}
  .man__body{left:68px;top:184px;width:200px;font-size:13px;line-height:19px}

  /* Spread 3 – Problem */
  .spread--problem{left:627px;top:420px;width:543px;height:273px}
  .problem__words{position:absolute;left:2px;top:-6px;font:800 34px/37px "Raleway",sans-serif;letter-spacing:10px;color:rgba(255,255,255,.55);white-space:nowrap}
  .problem__words span{display:block}
  .problem__words span:nth-child(2){opacity:.75}
  .problem__words span:nth-child(3){opacity:.55}
  .problem__words span:nth-child(4){opacity:.38}
  .problem__words span:nth-child(5){opacity:.22}
  .problem__bar{position:absolute;left:62px;top:0;width:27px;height:76px;background:var(--accent-blue)}
  .problem__heading{position:absolute;left:52px;top:152px;font:700 13.5px/1 "Raleway",sans-serif;color:var(--accent-blue)}
  .problem__body{left:24px;top:176px;width:245px;font-size:9.6px;line-height:16px;letter-spacing:.3px;text-align:justify}
  .dots{position:absolute}

  /* Spread 4 – Savior */
  .spread--savior{left:237px;top:763px;width:540px;height:275px}
  .savior__label{left:8px;top:155px;height:56px;font-size:42px}
  .savior__cross{left:0;top:0;width:157px;height:100%}
  .savior__column{position:absolute;left:157px;top:0;right:0;bottom:0;background:var(--page-dark)}
  .savior__callout{position:absolute;left:0;top:0;right:0;height:77px;background:var(--accent-blue);font:800 12.5px/16px "Raleway",sans-serif;text-align:center;padding-top:8px;letter-spacing:.5px}
  .savior__body{left:8px;top:94px;width:98px;font-size:9.4px;line-height:14.5px;text-transform:uppercase;text-align:center;letter-spacing:.4px}
  .savior__body b{font-weight:800}
  .savior__body em{font-style:normal;font-weight:800;color:var(--accent-blue)}
</style>
</head>
<body>

<section class="cover" aria-label="Front cover">
  <div class="cover__sky" role="img" aria-label="Photograph of bright blue sky and clouds with a figure with outstretched arms"></div>
  <div class="cover__frame"></div>
  <div class="cover__quote">”</div>
  <h1 class="cover__title">SUN</h1>
  <p class="cover__subtitle">On Water...</p>
</section>

<section class="spread spread--god" aria-label="God spread">
  <div class="page">
    <div class="photo fill" role="img" aria-label="Black and white photograph of a cross on a hill with the sun shining behind it"></div>
    <div class="label label--teal god__label">GOD</div>
  </div>
  <div class="page">
    <div class="photo photo--teal" style="left:0;top:0;width:190px;height:120px" role="img" aria-label="Blue-toned photograph of a hand reaching toward the light"></div>
    <div class="god__script">Sun</div>
    <div class="god__kicker">ON WATER,</div>
    <p class="body god__body">that means He's perfect. In fact, He is so perfect, corruption cannot live with Him.</p>
    <div class="rule" style="left:2px;top:253px;width:74px"></div>
  </div>
</section>

<section class="spread spread--man" aria-label="Man spread">
  <div class="page">
    <div class="photo fill" role="img" aria-label="Black and white photograph of a man leaning on a wall holding a book"></div>
  </div>
  <div class="page">
    <div class="photo photo--teal" style="left:0;top:0;width:189px;height:127px" role="img" aria-label="Blue-toned photograph of a church interior with arched windows"></div>
    <h2 class="man__heading">On the other hand,</h2>
    <p class="body man__body">mankind is corrupt.<br>For example, we are selfish, we are prideful, and we lie.</p>
    <div class="rule" style="left:137px;top:253px;width:130px"></div>
  </div>
  <div class="label label--teal man__label">MAN</div>
</section>

<section class="spread spread--problem" aria-label="Problem spread">
  <div class="page">
    <div class="photo fill" role="img" aria-label="Black and white photograph of a man with his head bowed"></div>
    <div class="problem__words" aria-hidden="true">
      <span>PROBLEM</span><span>PROBLEM</span><span>PROBLEM</span><span>PROBLEM</span><span>PROBLEM</span>
    </div>
  </div>
  <div class="page">
    <svg class="dots" style="left:8px;top:10px" width="60" height="110" aria-hidden="true">
      <g fill="var(--dot)">
        <circle cx="4" cy="4" r="1.3"/><circle cx="20" cy="4" r="1.3"/><circle cx="36" cy="4" r="1.3"/>
        <circle cx="4" cy="24" r="1.3"/><circle cx="20" cy="24" r="1.3"/><circle cx="36" cy="24" r="1.3"/>
        <circle cx="4" cy="44" r="1.3"/><circle cx="20" cy="44" r="1.3"/><circle cx="36" cy="44" r="1.3"/>
        <circle cx="4" cy="64" r="1.3"/><circle cx="20" cy="64" r="1.3"/><circle cx="36" cy="64" r="1.3"/>
        <circle cx="4" cy="84" r="1.3"/><circle cx="20" cy="84" r="1.3"/><circle cx="36" cy="84" r="1.3"/>
      </g>
    </svg>
    <div class="problem__bar"></div>
    <div class="photo" style="left:89px;top:0;right:0;height:139px" role="img" aria-label="Black and white photograph of a person praying with folded hands"></div>
    <h2 class="problem__heading">And there is our big problem:</h2>
    <p class="body problem__body">if God is perfect and corruption cannot live with him....and we are corrupt....WE cannot live with God. Our corruption has cut us off from God...now....AND when we die which means we must spend eternity in a place called hell...</p>
  </div>
</section>

<section class="spread spread--savior" aria-label="Savior spread">
  <div class="page">
    <div class="photo photo--teal fill" role="img" aria-label="Blue-toned photograph of a robed figure with open arms in the clouds above a father and child"></div>
    <div class="label label--dark savior__label">SAVIOR</div>
  </div>
  <div class="page">
    <div class="photo savior__cross" role="img" aria-label="Black and white photograph of crosses silhouetted on a hill"></div>
    <div class="savior__column">
      <div class="savior__callout">BUT THAT<br>IS NOT<br>WHAT GOD<br>WANTS.</div>
      <p class="body savior__body"><b>GOD LOVES YOU</b> so much he gave up his only son <em>to save you.</em> The Son died on the cross in our place to pay for our sin and rose again on the 3rd day.</p>
      <svg class="dots" style="left:12px;top:256px" width="92" height="12" aria-hidden="true">
        <g fill="var(--dot)">
          <circle cx="3" cy="3" r="1.2"/><circle cx="15" cy="3" r="1.2"/><circle cx="27" cy="3" r="1.2"/><circle cx="39" cy="3" r="1.2"/><circle cx="51" cy="3" r="1.2"/><circle cx="63" cy="3" r="1.2"/><circle cx="75" cy="3" r="1.2"/><circle cx="87" cy="3" r="1.2"/>
        </g>
      </svg>
    </div>
  </div>
</section>

</body>
</html>
```